Need App for Impact Related Events

My app is to help with internal events. When you enter the prompted event code the next screen shows you everyone currently at the event. It will give you the ability to Start a conversation with someone you met at that event, or signal it is your turn to send a message. The next screen is a message thread with that person. I am looking for a design that incorporates the colors and ‘feel good’ emotion of our logo. I have pieced together a pretty good interpretation of what I’m looking for in the attached mockup by slicing and dicing designs. I also attached our logo mascot.Screens (see attached mockups)

Note 1: I do not like the picture on the screen used in screen one because it makes it seem like a dating app. I attached an alternative photo that can be used or present different ideas.

Note 2: On the login/signup screen (screen 2) I need an additional first and last name for login, you can try to fit this on one login screen or present a two step signup screen where that is presented in the second screen.

READ MOCKUP GUIDELINES UNDER Must Haves

Target Market(s)

People attending internal social impact events

Industry/Entity Type

Charity

Font styles to use
Sans Serif

Colors
86cfc6

Requirements
Must have
• Follow the screen mockups attached to project
• PLEASE READ
• I have provided a relatively close design of what I’m looking for in the mockups. Some screens need to be followed more closely to my design mockup than other. I have listed a guide below how how closely you should follow my mockup design exactly. Overall I would like to see some ideas of incorporating a few accent colors so it doesn’t appear SO Blue. I also attached some app inspiration designs I found from around the web
• Screen Mockup Guideline Follow %
• Screen 1: 65% - mostly on target, would like to see ways to make it not SO Blue and possibly creative places to add some explainer text describing the app
• Screen 2: 50% - general design idea is here, but more open
• Screen 3: 35% - a lot more room for design influence
• Screen 4: 70% - mostly on target, a little room for design influence/color scheme ideas
• Screen 5-6: 25% - a lot of room for design change/ideas/influence
• Screen 7-8: 80% - already very close to what I need, maybe open to slight sizing and color scheme ideas
• Screen 9: 15% - the most open for influence, only the general functionality of the screen is communicated here
Nice to have
• Please Read Mockup Guideline above. In large part I am looking for something to use some nice accent colors so it is not overwhelmingly blue and bring the whole design into a seamless style.
Should not have

```html
<!DOCTYPE html>
<html lang="en">
<head>
<meta charset="utf-8">
<title>GoodHive – app screens</title>
<link href="https://fonts.googleapis.com/css2?family=Hind:wght@300;400;500;600&display=swap" rel="stylesheet">
<style>
:root{
  --bg:#efefef;
  --teal:#1fc6c9;
  --mint:#86cfc6;
  --mint-soft:#e3f7f4;
  --ink:#1e1e1e;
  --text:#4a4a4a;
  --muted:#8a8a8a;
  --panel:#ffffff;
  --soft:#f4f5f7;
  --bubble:#ececee;
}
*{box-sizing:border-box;margin:0;padding:0}
html,body{width:1200px;height:1200px;overflow:hidden;background:var(--bg);font-family:"Hind",sans-serif;color:var(--text)}
.board{position:relative;width:1200px;height:1200px}
.brand{position:absolute;left:740px;top:185px;display:flex;align-items:center;gap:14px}
.brand-dot{width:34px;height:34px;border-radius:50%;background:var(--teal)}
.brand-name{font-size:58px;font-weight:500;color:var(--ink);letter-spacing:1px;line-height:1}
.step{position:absolute;top:386px;width:40px;text-align:center;font-size:19px;font-weight:600;color:var(--ink)}
.screen{position:absolute;top:452px;width:234px;height:508px;background:var(--panel);border-radius:26px;overflow:hidden;box-shadow:0 6px 24px rgba(0,0,0,.06)}
.status{position:absolute;top:10px;left:20px;font-size:11px;color:var(--muted)}
.status-icons{position:absolute;top:13px;right:16px;width:36px;height:6px;background:linear-gradient(90deg,#bbb 0 30%,transparent 30% 42%,#bbb 42% 62%,transparent 62% 72%,#bbb 72%);border-radius:2px}
.home-bar{position:absolute;bottom:10px;left:50%;width:84px;height:3px;margin-left:-42px;border-radius:2px;background:#bdbdbd}
.deco{position:absolute;border-radius:50%;background:var(--mint-soft)}
.mascot-spot{position:absolute;width:34px;height:34px;margin:-17px 0 0 -17px;border-radius:50%;background:var(--teal)}
.heading{position:absolute;left:0;right:0;text-align:center;font-size:13px;font-weight:500;letter-spacing:.6px;color:var(--text)}
.field{position:absolute;left:22px;width:190px;height:40px;background:#fff;border-radius:4px;box-shadow:0 3px 12px rgba(0,0,0,.08);display:flex;align-items:center;justify-content:center;font-size:12px;color:var(--ink)}
.code{font-size:18px;font-weight:500;letter-spacing:1px}
.go{position:absolute;left:84px;top:301px;width:66px;height:66px;border-radius:50%;background:linear-gradient(135deg,#35d9c9,#1fb8c3);box-shadow:0 8px 18px rgba(31,198,201,.35);display:flex;align-items:center;justify-content:center}
.explain{position:absolute;left:10px;right:10px;top:283px;text-align:center;font-size:11.5px;line-height:19px;letter-spacing:.3px;color:var(--text)}
.list{height:550px;background:var(--soft)}
.list .top{position:absolute;left:0;top:0;width:100%;height:92px;background:#fff}
.back{position:absolute;left:12px;top:45px}
.title{position:absolute;top:42px;font-size:13px;font-weight:500;letter-spacing:.6px;color:var(--text)}
.search{position:absolute;left:8px;top:92px;width:217px;height:30px;background:#fff;border-radius:15px;box-shadow:0 3px 10px rgba(0,0,0,.06);display:flex;align-items:center;padding-left:14px;gap:10px;font-size:9.5px;color:var(--muted)}
.search .sep{width:1px;height:14px;background:#ddd}
.caption{position:absolute;left:16px;top:136px;font-size:9.5px;color:var(--text)}
.person{position:absolute;left:8px;width:217px;height:55px;background:#fff;border-radius:3px;border-left:3px solid var(--accent);box-shadow:0 3px 10px rgba(0,0,0,.05)}
.avatar{position:absolute;width:36px;height:36px;border-radius:50%;background:linear-gradient(135deg,#c9b8a8,#6f5d52)}
.person .avatar{left:12px;top:9px}
.presence{position:absolute;width:9px;height:9px;border-radius:50%;background:var(--teal);border:1.5px solid #fff}
.person .presence{left:41px;top:8px}
.presence.away{background:#cfcfcf}
.pname{position:absolute;left:57px;top:16px;font-size:13px;color:var(--text);white-space:nowrap}
.pname.with-sub{top:9px}
.psub{position:absolute;left:59px;top:31px;font-size:7.5px;color:var(--muted);white-space:nowrap}
.action{position:absolute;right:8px;top:11px;width:40px;text-align:center;font-size:7.5px;color:var(--text);white-space:nowrap}
.chev{position:absolute;right:26px;top:21px}
.more{position:absolute;left:0;right:0;top:500px;text-align:center;font-size:13px;font-weight:500;letter-spacing:.6px;color:var(--text)}
.chat{background:var(--soft)}
.chat .top{position:absolute;left:0;top:0;width:100%;height:92px;background:#fff;box-shadow:0 2px 8px rgba(0,0,0,.04)}
.chat-avatar{position:absolute;left:91px;top:67px;width:52px;height:52px;border-radius:50%;border:2px solid var(--teal);background:linear-gradient(135deg,#e5c3a6,#7b4a35)}
.chat-avatar .presence{right:-2px;top:0}
.bubble{position:absolute;font-size:9.5px;line-height:14px;padding:0 12px;display:flex;align-items:center;border-radius:5px;color:var(--text)}
.bubble.in{left:11px;width:187px;height:40px;background:var(--bubble)}
.bubble.out{left:38px;width:186px;height:42px;background:#fff}
.stamp{position:absolute;font-size:8px;color:var(--text)}
.stamp.left{left:16px}
.stamp.right{right:10px}
.composer{position:absolute;left:0;bottom:0;width:100%;height:62px;background:#fff}
.composer .input{position:absolute;left:14px;right:16px;top:8px;height:24px;border-bottom:1px solid #e3e3e3;font-size:10px;color:var(--muted);padding-left:7px;display:flex;align-items:center}
.composer svg{position:absolute;right:6px;top:2px}
</style>
</head>
<body>
<div class="board">

  <div class="brand"><span class="brand-dot"></span><span class="brand-name">GoodHive</span></div>

  <div class="step" style="left:141px">5</div>
  <div class="step" style="left:435px">6</div>
  <div class="step" style="left:726px">7</div>
  <div class="step" style="left:1021px">8</div>

  <section class="screen" style="left:44px">
    <div class="deco" style="left:190px;top:-20px;width:90px;height:90px;opacity:.6"></div>
    <div class="deco" style="left:142px;top:46px;width:18px;height:18px"></div>
    <div class="deco" style="left:192px;top:366px;width:110px;height:110px"></div>
    <div class="deco" style="left:3px;top:401px;width:18px;height:18px;background:#d3f3ef"></div>
    <div class="deco" style="left:37px;top:406px;width:8px;height:8px;background:#d3f3ef"></div>
    <span class="status">9:41</span><span class="status-icons"></span>
    <span class="mascot-spot" style="left:119px;top:107px"></span>
    <div class="heading" style="top:200px">ENTER LOCATION KIND CODE</div>
    <div class="field" style="top:234px">Enter code here</div>
    <div class="go">
      <svg width="26" height="18" viewBox="0 0 26 18"><path d="M1 9h23M16 1l8 8-8 8" fill="none" stroke="#fff" stroke-width="2" stroke-linecap="round" stroke-linejoin="round"/></svg>
    </div>
    <span class="home-bar"></span>
  </section>

  <section class="screen list" style="left:340px">
    <div class="top"></div>
    <span class="status">9:41</span><span class="status-icons"></span>
    <svg class="back" width="8" height="12" viewBox="0 0 8 12"><path d="M7 1L2 6l5 5" fill="none" stroke="var(--teal)" stroke-width="1.6"/></svg>
    <div class="title" style="left:36px">WHO YOU’VE MET SO FAR</div>
    <span class="mascot-spot" style="left:168px;top:74px;width:16px;height:16px;margin:-8px 0 0 -8px"></span>
    <div class="search">
      <svg width="12" height="12" viewBox="0 0 12 12"><circle cx="5" cy="5" r="4" fill="none" stroke="#9a9a9a" stroke-width="1.2"/><path d="M8 8l3 3" stroke="#9a9a9a" stroke-width="1.2"/></svg>
      <span class="sep"></span>Search here
    </div>
    <div class="caption">Who you’ve met so far</div>

    <div class="person" style="top:159px;--accent:#8fb6ff">
      <span class="avatar" role="img" aria-label="Profile photo of Nora J. Hale"></span><span class="presence"></span>
      <span class="pname">Nora J. Hale</span>
      <div class="action"><svg width="16" height="14" viewBox="0 0 16 14"><path d="M1 6L15 1 11 13 8 8z" fill="var(--teal)"/></svg><br>Start</div>
    </div>
    <div class="person" style="top:225px;--accent:#e27ad8">
      <span class="avatar" role="img" aria-label="Profile photo of Clara Moss" style="background:linear-gradient(135deg,#e5c3a6,#7b4a35)"></span><span class="presence"></span>
      <span class="pname">Clara Moss</span>
      <div class="action"><svg width="12" height="14" viewBox="0 0 12 14"><path d="M3 13V5a3 3 0 016 0v3M6 6l3 3 3-3" fill="none" stroke="var(--teal)" stroke-width="1.8"/></svg><br>Your Turn</div>
    </div>
    <div class="person" style="top:290px;--accent:#f4a06a">
      <span class="avatar" role="img" aria-label="Profile photo of Owen R. Pike" style="background:linear-gradient(135deg,#b7a898,#3e4b5c)"></span><span class="presence away"></span>
      <span class="pname with-sub">Owen R. Pike</span><span class="psub">Lorem Ipsum is simply dum...</span>
      <svg class="chev" width="6" height="10" viewBox="0 0 6 10"><path d="M1 1l4 4-4 4" fill="none" stroke="#777" stroke-width="1.2"/></svg>
    </div>
    <div class="person" style="top:356px;--accent:#9b7bdc">
      <span class="avatar" role="img" aria-label="Profile photo of Miles T. Carver" style="background:linear-gradient(135deg,#d2b49a,#2f2a2a)"></span><span class="presence"></span>
      <span class="pname with-sub">Miles T. Carver</span><span class="psub">Standard dummy text ever ...</span>
      <svg class="chev" width="6" height="10" viewBox="0 0 6 10"><path d="M1 1l4 4-4 4" fill="none" stroke="#777" stroke-width="1.2"/></svg>
    </div>
    <div class="person" style="top:422px;--accent:#8e7be0">
      <span class="avatar" role="img" aria-label="Profile photo of Theo Lindqvist" style="background:linear-gradient(135deg,#c5ab95,#4a3a33)"></span><span class="presence"></span>
      <span class="pname with-sub">Theo Lindqvist</span><span class="psub">Standard dummy text ever ...</span>
      <svg class="chev" width="6" height="10" viewBox="0 0 6 10"><path d="M1 1l4 4-4 4" fill="none" stroke="#777" stroke-width="1.2"/></svg>
    </div>
    <div class="more">TAP TO LOAD MORE (65)</div>
    <span class="home-bar"></span>
  </section>

  <section class="screen chat" style="left:633px">
    <div class="top"></div>
    <span class="status">9:41</span><span class="status-icons"></span>
    <svg class="back" width="8" height="12" viewBox="0 0 8 12"><path d="M7 1L2 6l5 5" fill="none" stroke="var(--teal)" stroke-width="1.6"/></svg>
    <div class="heading" style="top:42px">CLARA MOSS</div>
    <div class="chat-avatar" role="img" aria-label="Profile photo of Clara Moss"><span class="presence"></span></div>
    <div class="bubble in" style="top:138px">Who you’ve met so far</div>
    <span class="stamp left" style="top:184px">1 day ago</span>
    <div class="bubble out" style="top:200px">Lorem Ipsum has been the industry’s standard dummy text ever</div>
    <span class="stamp right" style="top:249px">1 day ago</span>
    <div class="bubble in" style="top:269px">Who you’ve met so far</div>
    <span class="stamp left" style="top:315px">1 day ago</span>
    <div class="bubble out" style="top:331px">Lorem Ipsum has been the industry’s standard dummy text ever</div>
    <span class="stamp right" style="top:381px">1 day ago</span>
    <div class="composer">
      <div class="input">Type your message here
        <svg width="16" height="14" viewBox="0 0 16 14"><path d="M1 6L15 1 11 13 8 8z" fill="var(--teal)"/></svg>
      </div>
    </div>
    <span class="home-bar"></span>
  </section>

  <section class="screen" style="left:931px">
    <div class="deco" style="left:186px;top:-20px;width:90px;height:90px;opacity:.6"></div>
    <div class="deco" style="left:142px;top:38px;width:18px;height:18px"></div>
    <div class="deco" style="left:192px;top:366px;width:110px;height:110px"></div>
    <div class="deco" style="left:3px;top:401px;width:18px;height:18px;background:#d3f3ef"></div>
    <div class="deco" style="left:37px;top:406px;width:8px;height:8px;background:#d3f3ef"></div>
    <span class="mascot-spot" style="left:117px;top:107px"></span>
    <div class="heading" style="top:193px">YOUR KIND CODE</div>
    <div class="field code" style="top:226px">JGHEYS747JRH</div>
    <p class="explain">Give this code to the people<br>at your location or event to allow<br>them to connect to each<br>other - kind of like a wifi password</p>
    <span class="home-bar"></span>
  </section>

</div>
</body>
</html>
```